Veltrix Stationary

Design the stationary of Veltrix Promotions Group.

Veltrix is a BTL company, BTL meaning "below the line". In other words Veltrix is a Promotional Marketing company (the company that design the brands promotional activities).

The design should transmit creativity, agility, boldness.

I need:
* Bis Card
* Letter head
* Envelopes, both vertical and horizontal (for legal size), and letter envelope
* Folders
* PPT template (Title page and regular page)
* CD slip (CD envelope)
* ID card (employee card)

And what ever else you want to throw in.
Updates

Guys,

Something I missed from the brief.   The predominat color should be RED.

Also, have fun and play with the exclamation mark (!) of the logo. 

Hi guys, more comments:

Remember that Veltrix is a "creativity" agency, not in the advertising side but on the promotional side, and that should reflect on the stationary.

 I want a bold design.  Bold and yet crisp.

 

Guys, i just uploaded the Logo in AI format.

I Also uploaded the actual Veltrix Bis Card, wich I like.  So I will like to see some designs with that bis card approach.

Guys, I am so sorry, but I notice in your last post that I upladed a wrong design ("13154_marketing_group_veltrix_brief225630.ai").  The problem was that I asked the designer the file in AI format and he send me thw wrong file, and since I dont have Illustrator I could not verify it.

The differences are minor, I just already ask him the correct one (similar to the EPS file).

Sorry                                   

Just post the correct AI file : "Veltrix Logo.ai"

Reason: I'm expecting more designs to choose from and also I wont be available tomorrow to decide.

Reason: Sorry guys, but we are not there yet!

Target Market(s)

Marketing directors, Marketing Managers

Industry/Entity Type

Legal

Requirements
Must have
• Must work with the logo attached.
The predominat color should be RED.
Play and have fun with the exclamation mark (!).
Should not have
• * No old fonts

Should not be:
* boring
* Informal
* rigid

```html
<!DOCTYPE html>
<html lang="en">
<head>
<meta charset="utf-8">
<title>Veltrix Promotions Group – Stationery</title>
<link rel="stylesheet" href="https://fonts.googleapis.com/css2?family=Open+Sans:wght@400;600;800&display=swap">
<style>
  :root {
    --backdrop: #2b2b2b;
    --paper: #ffffff;
    --brand-red: #d71a21;
    --brand-red-deep: #c4151c;
    --brand-red-soft: #e0252c;
    --ink: #222222;
    --band-grey: #7d7d7d;
    --band-grey-dark: #5e5e5e;
    --divider: #555555;
  }
  * { margin: 0; padding: 0; box-sizing: border-box; }
  html, body {
    width: 1200px;
    height: 900px;
    overflow: hidden;
    background: var(--backdrop);
    font-family: "Open Sans", Arial, sans-serif;
  }
  .stage { position: relative; width: 1200px; height: 900px; }

  /* Letterhead */
  .letterhead {
    position: absolute;
    left: 93px; top: 153px;
    width: 464px; height: 602px;
    background: var(--paper);
  }
  .letterhead__brand {
    position: absolute;
    left: 32px; top: 26px;
    display: flex; align-items: center; gap: 6px;
  }
  .brand-name {
    font-weight: 800;
    font-size: 28px;
    line-height: 1;
    letter-spacing: -0.5px;
    color: var(--ink);
  }
  .brand-mark {
    width: 9px; height: 9px;
    background: var(--brand-red);
  }
  .letterhead__footer {
    position: absolute;
    left: 45px; top: 548px;
    display: flex;
    font-size: 6.5px;
    line-height: 8px;
    color: var(--ink);
  }
  .footer-col { padding-right: 14px; }
  .footer-col + .footer-col {
    border-left: 1px solid var(--divider);
    padding-left: 12px;
  }
  .footer-col--address { width: 96px; }
  .footer-label { color: var(--brand-red); font-weight: 600; }
  .letterhead__band {
    position: absolute;
    left: 34px; top: 578px;
    width: 398px; height: 13px;
    background: linear-gradient(180deg, var(--band-grey) 0%, var(--band-grey-dark) 100%);
    border-radius: 0 0 8px 8px;
  }
  .letterhead__accent {
    position: absolute;
    left: 344px; top: 526px;
    width: 90px; height: 58px;
    background: linear-gradient(135deg, var(--brand-red-soft) 0%, var(--brand-red) 100%);
    border-radius: 4px 4px 14px 4px;
  }

  /* Folder */
  .folder {
    position: absolute;
    left: 678px; top: 140px;
    width: 462px; height: 600px;
    background: var(--brand-red);
  }
  .folder__pattern {
    position: absolute; inset: 0;
    background: linear-gradient(160deg, var(--brand-red-soft) 0%, var(--brand-red) 45%, var(--brand-red-deep) 100%);
  }
  .folder__brand {
    position: absolute;
    left: 0; right: 0; top: 264px;
    display: flex; justify-content: center; align-items: center; gap: 10px;
  }
  .folder__brand .brand-name { color: var(--paper); font-size: 42px; }
  .folder__brand .brand-mark { background: var(--paper); width: 13px; height: 13px; }
</style>
</head>
<body>
<main class="stage">
  <section class="letterhead" aria-label="Letterhead">
    <div class="letterhead__brand">
      <span class="brand-name">veltrix</span>
      <span class="brand-mark"></span>
    </div>
    <footer class="letterhead__footer">
      <div class="footer-col footer-col--address">
        Veltrix Promotions Group<br>Street, Region, Country<br>PO BOX 321
      </div>
      <div class="footer-col">
        <span class="footer-label">P</span> +31 (6) 48 20 71 35<br>
        <span class="footer-label">F</span> +31 (6) 48 20 71 36
      </div>
      <div class="footer-col">
        <span class="footer-label">E</span> info@veltrixpromo.com<br>
        <span class="footer-label">W</span> www.veltrixpromo.com
      </div>
    </footer>
    <div class="letterhead__band"></div>
    <div class="letterhead__accent" role="img" aria-label="Bold red exclamation-mark accent lying across the footer band"></div>
  </section>

  <section class="folder" aria-label="Presentation folder">
    <div class="folder__pattern" role="img" aria-label="Tone-on-tone red repeating exclamation-mark pattern"></div>
    <div class="folder__brand">
      <span class="brand-name">veltrix</span>
      <span class="brand-mark"></span>
    </div>
  </section>
</main>
</body>
</html>
```